Property Management business needs Business cards designed

We provide a premium property management service based in Sydney's Norther Beaches. We want people to feel confident in choosing us to manage their investment properties. We offer a much more personalized service than other estate agents.
We want a modern clean design. Something that shows confidence without being complicated.
Logo attached.

Target Market(s)

35-70yo Male and Female with strong property portfolios within Sydney's Norther Beaches

Industry/Entity Type

Property Management

Contact Information for Business Card

Address: Suite 7, 12-14 Kelvin Parade, Harlow NSW 2188
Two separate named cards.
Tom Ardley - 0491 570 118 tom@harbourvaleestates.com.au
Clara Dunmore - 0491 570 263 clara@harbourvaleestates.com.au

Requirements
Must have
• Business logo, name, number, address, email.

```html
<!DOCTYPE html>
<html lang="en">
<head>
<meta charset="utf-8">
<title>Harbourvale Estates – Business Card</title>
<link rel="stylesheet" href="https://fonts.googleapis.com/css2?family=Source+Sans+3:wght@400;600;700&display=swap">
<style>
  :root {
    --stage: #151515;
    --card: #ffffff;
    --ink: #111111;
    --teal: #1d7384;
    --teal-bright: #2a9aa6;
  }
  * { box-sizing: border-box; margin: 0; padding: 0; }
  html, body {
    width: 1200px; height: 900px; overflow: hidden;
    background: var(--stage);
    font-family: "Source Sans 3", Arial, sans-serif;
  }
  .card {
    position: absolute;
    background: var(--card);
    border-radius: 12px;
  }
  .card--front { left: 149px; top: 306px; width: 439px; height: 271px; }
  .card--back  { left: 608px; top: 306px; width: 441px; height: 272px; }

  .brand {
    position: absolute; left: 27px; top: 52px;
    display: flex; align-items: center; gap: 8px;
  }
  .brand__mark { width: 14px; height: 14px; background: var(--teal-bright); }
  .brand__name {
    font-size: 29px; font-weight: 700; color: var(--ink);
    letter-spacing: -0.3px; line-height: 1;
  }

  .contact { position: absolute; left: 188px; top: 143px; color: var(--ink); }
  .contact__name {
    font-size: 16px; font-weight: 600; color: var(--teal);
    margin-bottom: 12px;
  }
  .contact__address { font-size: 12.5px; line-height: 15px; margin-bottom: 14px; }
  .contact__line {
    display: flex; align-items: center; gap: 6px;
    font-size: 12.5px; line-height: 16px;
  }
  .contact__icon { width: 10px; height: 10px; fill: var(--teal); flex: none; }

  .back-brand {
    position: absolute; inset: 0;
    display: flex; align-items: center; justify-content: center; gap: 12px;
  }
  .back-brand__mark { width: 22px; height: 22px; border-radius: 50%; background: var(--teal-bright); }
  .back-brand__name { font-size: 32px; font-weight: 700; color: var(--teal); }
</style>
</head>
<body>
  <section class="card card--front">
    <div class="brand">
      <span class="brand__mark"></span>
      <span class="brand__name">HARBOURVALE ESTATES</span>
    </div>
    <div class="contact">
      <p class="contact__name">Tom Ardley</p>
      <p class="contact__address">Suite 7, 12-14 Kelvin Parade<br>Harlow NSW 2188</p>
      <p class="contact__line">
        <svg class="contact__icon" viewBox="0 0 10 10" aria-hidden="true"><path d="M2 0.5 3.6 2.6 2.7 3.6C3.3 5 4.8 6.6 6.3 7.3L7.4 6.3 9.5 8 8.3 9.5C4.5 9.2 0.8 5.6 0.5 1.7Z"/></svg>
        0491 570 118
      </p>
      <p class="contact__line">
        <svg class="contact__icon" viewBox="0 0 10 10" aria-hidden="true"><path d="M1 2.5h8v5.5H1z"/><path d="M1 2.5 5 5.5 9 2.5" fill="none" stroke="#fff" stroke-width="0.9"/></svg>
        tom@harbourvaleestates.com.au
      </p>
    </div>
  </section>

  <section class="card card--back">
    <div class="back-brand">
      <span class="back-brand__mark"></span>
      <span class="back-brand__name">HARBOURVALE ESTATES</span>
    </div>
  </section>
</body>
</html>
```